Pinewhistle Lodges Website

We need a revamp on our website. We would like to keep the same "vibe", the Brindlewood style, and all the content. But we need a more appealing website, with new pictures of everything.

Preferably done by Squarespace or Wix.

www.pinewhistlelodges.example

```html
<!DOCTYPE html>
<html lang="en">
<head>
<meta charset="utf-8">
<title>Pinewhistle Lodges</title>
<link rel="stylesheet" href="https://fonts.googleapis.com/css2?family=Dancing+Script:wght@700&family=Open+Sans:ital,wght@0,400;0,600;0,700;1,400&display=swap">
<style>
:root{
  --brown:#9b6a2b;
  --brown-dark:#7d5320;
  --green:#7aa11d;
  --green-light:#9cc43a;
  --ink:#2b2b2b;
  --muted:#777;
  --footer:#232323;
  --footer-line:#3a3a3a;
  --white:#fff;
}
*{box-sizing:border-box;margin:0;padding:0}
html,body{width:1200px;height:3358px;overflow:hidden}
body{font-family:"Open Sans",Arial,sans-serif;color:var(--ink);background:var(--white)}
.page{position:relative;width:1200px;height:3358px;overflow:hidden}
.abs{position:absolute}
.script{font-family:"Dancing Script",cursive;font-weight:700}

/* header */
.site-header{left:0;top:0;width:1200px;height:170px;background:var(--brown)}
.brand{left:0;top:26px;width:1200px;display:flex;justify-content:center;align-items:center;gap:14px}
.brand-dot{width:32px;height:32px;border-radius:50%;background:#3b2a14}
.brand-name{font-weight:700;font-size:32px;letter-spacing:2px;color:#3b2a14;text-transform:uppercase}
.main-nav{left:0;top:126px;width:1200px;display:flex;justify-content:center;gap:46px;font-size:15px;color:var(--white)}
.main-nav .active{color:var(--green-light);border-bottom:2px solid var(--green-light);padding-bottom:4px}

/* hero */
.hero{left:0;top:170px;width:1200px;height:560px;background:linear-gradient(180deg,#3a3d2c 0%,#4d4432 45%,#2f2e24 100%)}
.hero-shade{left:0;top:170px;width:1200px;height:560px;background:linear-gradient(90deg,rgba(0,0,0,.45),rgba(0,0,0,0) 60%)}
.hero-title{left:130px;top:284px;font-size:38px;line-height:46px;color:var(--white)}
.hero-quote{left:134px;top:402px;font-size:16px;font-style:italic;line-height:24px;color:var(--white)}
.btn-ghost{left:134px;top:496px;width:140px;height:40px;border:2px solid var(--white);color:var(--white);font-size:14px;display:flex;align-items:center;justify-content:center}
.slider-arrow{width:32px;height:32px;border:2px solid var(--white);display:flex;align-items:center;justify-content:center}

/* booking */
.booking{left:122px;top:686px;width:956px;height:116px;background:var(--brown);padding:10px}
.booking-inner{width:100%;height:100%;border:2px solid #d9b98a;display:flex;align-items:center;gap:10px;padding:0 20px}
.field{height:42px;background:var(--white);border:1px solid #ccc;flex:0 0 166px;display:flex;align-items:center;justify-content:space-between;padding:0 10px;font-family:"Dancing Script",cursive;font-size:16px;color:#555}
.btn-check{flex:0 0 200px;height:42px;background:var(--green);color:var(--white);font-weight:700;font-size:15px;display:flex;align-items:center;justify-content:center;margin-left:6px}

/* welcome */
.welcome{left:0;top:730px;width:1200px;height:510px;background:linear-gradient(180deg,#eeeeea,#f6f6f3)}
.palm{left:890px;top:800px;width:230px;height:340px;background:radial-gradient(ellipse at 45% 30%,#5a9a2b 0%,rgba(90,154,43,.5) 45%,rgba(90,154,43,0) 72%)}
.section-title{font-size:28px;color:var(--ink)}
.section-sub{font-size:12px;font-style:italic;color:#555}
.title-rule{height:3px;background:var(--green)}
.welcome-text{left:122px;top:926px;width:860px;font-size:13px;line-height:22px;color:#555}
.room-card{top:1024px;width:296px;height:158px;background:var(--white);border:1px solid #d4d4d4;padding:6px}
.room-card-inner{width:100%;height:100%;border:1px dashed var(--green-light);display:flex;flex-direction:column;align-items:center;justify-content:center;gap:12px}
.room-icon{width:58px;height:58px;border-radius:50%;background:var(--green);display:flex;align-items:center;justify-content:center}
.room-name{font-size:24px}
.room-card.featured{background:var(--green);border-color:var(--green)}
.room-card.featured .room-card-inner{border-color:#d6e9a6;color:var(--white);text-align:center}
.room-card.featured p{font-size:13px;line-height:19px}
.ivy{left:0;top:1115px;width:410px;height:220px;background:radial-gradient(ellipse at 40% 55%,#4f9a2e 0%,rgba(79,154,46,.45) 40%,rgba(79,154,46,0) 70%)}

/* house info */
.house-card{top:1405px;width:297px;height:222px;background:var(--white);box-shadow:0 2px 6px rgba(0,0,0,.18)}
.house-photo{width:100%;height:160px}
.house-meta{height:62px;display:flex;align-items:center;justify-content:space-between;padding:0 16px}
.house-name{font-size:18px}
.house-price{text-align:right;font-size:15px;line-height:16px}
.house-price small{display:block;font-size:11px;font-style:italic;color:#999}
.house-card.featured .house-meta{background:#1d2a4a;color:var(--white)}
.house-card.featured .house-price{color:#f1c40f}
.house-card.featured .house-price small{color:var(--white)}
.mini-arrow{width:24px;height:24px;border:2px solid var(--green);display:flex;align-items:center;justify-content:center}

/* about */
.about-photo{left:0;top:1683px;width:548px;height:318px;background:linear-gradient(160deg,#5b6b4a 0%,#6e4a30 55%,#3e3a2b 100%)}
.about-panel{left:548px;top:1683px;width:652px;height:318px;background:var(--brown);padding:40px 56px 0 56px;color:var(--white)}
.about-panel .section-sub{color:#f4d08a}
.about-panel p.body{margin-top:18px;font-size:11.5px;line-height:20px;color:#f3e6d2}

/* testimonials */
.leaf-left{left:215px;top:2040px;width:210px;height:230px;background:radial-gradient(ellipse at 50% 40%,#4c8a2a 0%,rgba(76,138,42,.4) 45%,rgba(76,138,42,0) 72%)}
.leaf-right{left:770px;top:2210px;width:220px;height:250px;background:radial-gradient(ellipse at 50% 55%,#5f9a2e 0%,rgba(95,154,46,.4) 45%,rgba(95,154,46,0) 72%)}
.testimonial{left:280px;top:2088px;width:640px;height:320px;background:var(--white);box-shadow:0 4px 18px rgba(0,0,0,.18);padding:30px 140px 0 140px;text-align:center}
.testimonial h2{font-size:28px;color:#3d7a1a}
.testimonial .rule{width:80px;height:3px;background:var(--green);margin:6px auto 24px}
.testimonial blockquote{font-size:13px;font-style:italic;line-height:23px;color:#555}
.reviewer{left:412px;top:2318px;display:flex;gap:12px;align-items:center}
.avatar{width:46px;height:46px;border-radius:50%;background:#8a7360}
.reviewer-name{font-size:13px;color:var(--ink)}
.reviewer-date{font-size:11px;color:#888}
.stars{color:#c1791f;font-size:13px;letter-spacing:3px}

/* banner */
.banner{left:0;top:2505px;width:1200px;height:322px;background:linear-gradient(180deg,#7b93a6 0%,#3b5266 40%,#1f3344 100%)}
.banner-quote{left:0;top:2596px;width:1200px;text-align:center;font-size:44px;line-height:52px;color:var(--white)}

/* newsletter */
.newsletter{left:0;top:2827px;width:1200px;height:115px;background:var(--brown)}
.newsletter h3{font-size:17px;font-weight:700;color:var(--white);text-transform:uppercase}
.newsletter p{font-size:12px;font-style:italic;color:#f3e6d2;margin-top:6px}
.email-input{left:562px;top:2862px;width:272px;height:42px;background:var(--white);font-size:12px;font-style:italic;color:#999;display:flex;align-items:center;padding-left:16px}
.btn-subscribe{left:906px;top:2862px;width:174px;height:42px;background:#2b2b2b;color:var(--white);font-size:13px;font-weight:700;display:flex;align-items:center;justify-content:space-between;padding:0 18px}

/* footer */
.site-footer{left:0;top:2942px;width:1200px;height:416px;background:var(--footer);color:#9a9a9a;font-size:12px}
.footer-col h4{font-size:13px;color:var(--white);text-transform:uppercase;font-weight:600;margin-bottom:18px}
.footer-col h4.script{text-transform:none;font-size:18px}
.footer-col li{list-style:none;line-height:24px}
.footer-col li.current{color:var(--green-light)}
.footer-col p{line-height:18px}
.contact-row{display:flex;gap:10px;line-height:18px;margin-bottom:12px}
.contact-row .label{color:var(--green-light)}
.social{display:flex;gap:20px;margin-top:34px}
.social span{width:20px;height:20px;border:2px solid #8a8a8a;border-radius:4px}
.footer-rule{left:122px;top:3287px;width:956px;height:1px;background:var(--footer-line)}
.copyright{left:0;top:3312px;width:1200px;text-align:center;font-size:12px;color:#9a9a9a}
</style>
</head>
<body>
<div class="page">

  <header class="site-header abs"></header>
  <div class="brand abs"><span class="brand-dot"></span><span class="brand-name">Pinewhistle Lodges</span></div>
  <nav class="main-nav abs">
    <span class="active">Home</span><span>About Us</span><span>Information ▾</span><span>Rates</span><span>Gallery</span><span>Offers</span><span>Dinning</span><span>Contact Us</span>
  </nav>

  <div class="hero abs" role="img" aria-label="Photo of a large timber lodge among tall pine trees with flags on the porch"></div>
  <div class="hero-shade abs"></div>
  <h1 class="hero-title abs script">Make Your Memorable<br>Holidays in a Pinewhistle Lodge</h1>
  <p class="hero-quote abs">"Nestled in two acres of pine trees in Brindlewood Vista, California,<br>The Pinewhistle Lodges are warm, clean and friendly."</p>
  <div class="btn-ghost abs">Know More</div>
  <div class="slider-arrow abs" style="left:46px;top:434px"><svg width="12" height="14" viewBox="0 0 12 14"><path d="M9 1 3 7l6 6" stroke="#fff" stroke-width="2" fill="none"/></svg></div>
  <div class="slider-arrow abs" style="left:1120px;top:434px"><svg width="12" height="14" viewBox="0 0 12 14"><path d="m3 1 6 6-6 6" stroke="#fff" stroke-width="2" fill="none"/></svg></div>

  <div class="welcome abs"></div>

  <form class="booking abs">
    <div class="booking-inner">
      <div class="field">Arrival Date <svg width="14" height="14"><rect x="1" y="2" width="12" height="11" fill="none" stroke="#777"/><path d="M1 5h12" stroke="#777"/></svg></div>
      <div class="field">Departure Date <svg width="14" height="14"><rect x="1" y="2" width="12" height="11" fill="none" stroke="#777"/><path d="M1 5h12" stroke="#777"/></svg></div>
      <div class="field">Adults <svg width="10" height="6"><path d="m1 1 4 4 4-4" stroke="#777" fill="none"/></svg></div>
      <div class="field">Children <svg width="10" height="6"><path d="m1 1 4 4 4-4" stroke="#777" fill="none"/></svg></div>
      <div class="btn-check">Check Availability</div>
    </div>
  </form>

  <div class="palm abs" role="img" aria-label="Illustration of a palm tree"></div>
  <h2 class="section-title script abs" style="left:122px;top:848px">Welcome to Pinewhistle Lodges</h2>
  <p class="section-sub abs" style="left:124px;top:888px">Pick a room that best suits your taste and budget</p>
  <div class="title-rule abs" style="left:434px;top:896px;width:80px"></div>
  <p class="welcome-text abs">The rooms are comprised of suites, stand-alone cottages and duplex cabins. With a variety of floor plans, we have warm, clean and cozy options to meet the needs of any sized family!</p>

  <div class="room-card abs" style="left:122px">
    <div class="room-card-inner">
      <div class="room-icon"><svg width="28" height="26" viewBox="0 0 28 26"><path d="M14 2 2 12h4v12h6v-7h4v7h6V12h4z" fill="#fff"/></svg></div>
      <div class="room-name script">Small Cottage</div>
    </div>
  </div>
  <div class="room-card featured abs" style="left:455px">
    <div class="room-card-inner">
      <div class="room-name script">Medium Cottage</div>
      <p>Small studio cottage with queen<br>bed and bath<br>Sleeps 2 max</p>
    </div>
  </div>
  <div class="room-card abs" style="left:788px">
    <div class="room-card-inner">
      <div class="room-icon"><svg width="30" height="24" viewBox="0 0 30 24"><path d="M4 22V10l6-6 5 5 5-5 6 6v12H4z" fill="#fff"/><rect x="9" y="14" width="4" height="8" fill="#7aa11d"/><rect x="17" y="14" width="4" height="8" fill="#7aa11d"/></svg></div>
      <div class="room-name script">Large Cottage</div>
    </div>
  </div>

  <div class="ivy abs" role="img" aria-label="Illustration of trailing ivy leaves"></div>

  <h2 class="section-title script abs" style="left:480px;top:1286px">House Information</h2>
  <p class="section-sub abs" style="left:482px;top:1332px">Pick a room that best suits your taste and budget</p>
  <div class="title-rule abs" style="left:790px;top:1340px;width:80px"></div>
  <div class="mini-arrow abs" style="left:1015px;top:1322px"><svg width="8" height="10"><path d="M6 1 2 5l4 4" stroke="#7aa11d" stroke-width="2" fill="none"/></svg></div>
  <div class="mini-arrow abs" style="left:1057px;top:1322px"><svg width="8" height="10"><path d="m2 1 4 4-4 4" stroke="#7aa11d" stroke-width="2" fill="none"/></svg></div>

  <article class="house-card abs" style="left:122px">
    <div class="house-photo" role="img" aria-label="Photo of Birdhouse, a green cabin among pines" style="background:linear-gradient(160deg,#4d6b4c,#2e3f2c)"></div>
    <div class="house-meta"><span class="house-name script">Birdhouse</span><span class="house-price">$369<small>Two Night</small></span></div>
  </article>
  <article class="house-card featured abs" style="left:455px">
    <div class="house-photo" role="img" aria-label="Photo of Meadow Vista, a log cabin in sunlit woods" style="background:linear-gradient(160deg,#b7b276,#5e4a2c)"></div>
    <div class="house-meta"><span class="house-name script">Meadow Vista</span><span class="house-price">$449<small>Two Night</small></span></div>
  </article>
  <article class="house-card abs" style="left:786px">
    <div class="house-photo" role="img" aria-label="Photo of Snow Creek Cabin, a wooden cabin in forest" style="background:linear-gradient(160deg,#6a7380,#4a3424)"></div>
    <div class="house-meta"><span class="house-name script">Snow Creek Cabin</span><span class="house-price">$399<small>Two Night</small></span></div>
  </article>

  <div class="about-photo abs" role="img" aria-label="Photo of timber lodge buildings with garages among pine trees"></div>
  <section class="about-panel abs">
    <h2 class="section-title script" style="color:#fff">Know About Us</h2>
    <p class="section-sub">Pick a room that best suits your taste and budget</p>
    <p class="body">"The Brindlewood Vista Lodge &amp; Cabins are located one mile west of the Pinewhistle Lodges, the Fernhallow Resort built between 1943 and 1947 by Alder J. Fenwick, this property has had many names and owners over the years. The resort was saved from wrecking ball February 2002. All of the interiors have refurbished and have private bathrooms, full kitchens, coffeemakers, televisions with premium movie channels and video tape/DVD players, and of course, wrought iron beds with nice linens. Although not all of the rooms are freestanding cabins, the property and rooms are overall larger than The Pinewhistle Lodges with choices of cabins, duplex cabins, and suites. The Brindlewood Vista Lodge also has a swimming pool, along with beach access."</p>
  </section>

  <div class="leaf-left abs" role="img" aria-label="Illustration of a palm leaf"></div>
  <section class="testimonial abs">
    <h2 class="script">Testimonials</h2>
    <div class="rule"></div>
    <blockquote>"This place is the definition of "hospitality". Funky, almost dilapidated cabins highlight the wonderful rustic feelings of being in the mountains, without sacrificing comfort or cleanliness. Complimentary breakfast, surrounded best."</blockquote>
  </section>
  <div class="reviewer abs">
    <div class="avatar" role="img" aria-label="Reviewer portrait"></div>
    <div><div class="reviewer-name">Owen Hartley</div><div class="reviewer-date">7 day ago</div><div class="stars">★★★★★</div></div>
  </div>
  <div class="mini-arrow abs" style="left:734px;top:2336px;width:22px;height:22px"><svg width="8" height="10"><path d="M6 1 2 5l4 4" stroke="#7aa11d" stroke-width="2" fill="none"/></svg></div>
  <div class="mini-arrow abs" style="left:764px;top:2336px;width:22px;height:22px"><svg width="8" height="10"><path d="m2 1 4 4-4 4" stroke="#7aa11d" stroke-width="2" fill="none"/></svg></div>
  <div class="leaf-right abs" role="img" aria-label="Illustration of a palm leaf"></div>

  <div class="banner abs" role="img" aria-label="Photo of a group paddleboarding on a mountain lake"></div>
  <p class="banner-quote abs script">A vacation is having nothing<br>to do &amp; all day to do it in</p>

  <section class="newsletter abs">
    <div class="abs" style="left:122px;top:38px">
      <h3>Stay Tuned With Us</h3>
      <p>Get our updated offers, discounts, events and much more!</p>
    </div>
  </section>
  <svg class="abs" style="left:500px;top:2856px" width="70" height="60" viewBox="0 0 70 60"><rect x="4" y="10" width="60" height="42" fill="none" stroke="#8a5c22" stroke-width="3"/><path d="m4 10 30 22 30-22" fill="none" stroke="#8a5c22" stroke-width="3"/></svg>
  <div class="email-input abs">Enter Your Email Address</div>
  <div class="btn-subscribe abs">SUBSCRIBE <span>→</span></div>

  <footer class="site-footer abs">
    <div class="footer-col abs" style="left:122px;top:70px;width:230px">
      <h4 class="script">Pinewhistle Lodges</h4>
      <p>The cottages are clean, comfortable and the Pinewhistle Lodges is a very friendly special place to stay.</p>
      <p style="color:var(--green-light);margin-top:18px">Read More ›</p>
      <div class="social"><span></span><span></span><span></span><span></span><span></span></div>
    </div>
    <div class="footer-col abs" style="left:430px;top:70px">
      <h4>Quick Links</h4>
      <ul><li class="current">Home</li><li>About Us</li><li>Rates</li><li>Gallery</li><li>Offer</li><li>Dinning</li><li>Contact Us</li></ul>
    </div>
    <div class="footer-col abs" style="left:626px;top:70px">
      <h4>Explore</h4>
      <ul><li>Small Cottage</li><li>Explore Cottage</li><li>Large Cottage</li><li>Birdhouse</li><li>Meadow Vista</li><li>Snow Creek</li><li>Duplex Cabin</li></ul>
    </div>
    <div class="footer-col abs" style="left:840px;top:70px;width:240px">
      <h4>Get In Touch</h4>
      <div class="contact-row"><svg width="12" height="16" viewBox="0 0 12 16"><path d="M6 1a5 5 0 0 0-5 5c0 4 5 9 5 9s5-5 5-9a5 5 0 0 0-5-5z" fill="none" stroke="#ccc" stroke-width="1.5"/><circle cx="6" cy="6" r="1.8" fill="#ccc"/></svg><div><span class="label">PINEWHISTLE LODGES,</span><br>210 Cedar Hollow Rd.,<br>P.O. Box 42,<br>Brindlewood, CA 90000</div></div>
      <div class="contact-row"><svg width="14" height="14" viewBox="0 0 14 14"><circle cx="7" cy="7" r="6" fill="none" stroke="#ccc" stroke-width="1.5"/><path d="M4.5 4.5c0 3 2 5 5 5l.5-1.5-1.5-.8-.8.8c-.8-.4-1.300-.9-1.700-1.700l.8-.8L6 4z" fill="#ccc"/></svg>1-555-014-2290</div>
      <div class="contact-row"><svg width="14" height="14" viewBox="0 0 14 14"><circle cx="7" cy="7" r="6" fill="none" stroke="#ccc" stroke-width="1.5"/><rect x="3.5" y="4.5" width="7" height="5" fill="none" stroke="#ccc"/><path d="m3.5 4.5 3.5 3 3.5-3" fill="none" stroke="#ccc"/></svg>hello@pinewhistlelodges.example</div>
    </div>
  </footer>
  <div class="footer-rule abs"></div>
  <p class="copyright abs">Copyright © 2019, Pinewhistle Lodges</p>

</div>
</body>
</html>
```